Three Banner Ad Concepts Multiple Sizes For Pixelhive Native Ads Network Campaigns

I would like to see THREE totally different concepts using the content below. Once I approve the THREE DESIGN CONCEPTS I will need them in 5 different sizes for each of the 3 approved concepts.

So technically I am asking for THREE totally different designs in FIVE Sizes. See Sizes below.

I will advertise these banners on zentrix ad display network, vimbly.com as well as pixelhive so please keep these in mind and if you have experience creating these type of ads then this is great.

Headlines:
1. Boost Responses To Your Ads Without Increasing Ad Spend Giving Away Free Smartwatches and Norvicks You Don't Personally Need To Fulfill!

2. Attract More Customers During Tough Times Giving Away Free Vacation & Dining Vouchers That You Don't Need To Pay For!

3. Increase Conversions On Your Website Offering A Free Hotel Stay Or Even A Smart Watch In Exchange For Their Form Submission!

Calls To Actions:
1. Get A Free Sample Package
2. Sign Up For A Free Trial
3. Book A Demo

Native Ads Sizes
Image Size 600x600
Image Size 600x500
Image Size 600x315

Pixelhive (for px ads please take into account the 20% text rule in the image):
For carousel: 1200x1200 pixels
For regular image ads: 1200x628 pixels

Target Market(s)

B2B, Small Business Owners, Entrepreneurs, Marketing Directors, Sales Managers

Industry/Entity Type

Marketing

Requirements
Must have
• Use images from lumarta.com as I have account here
Nice to have
• These designs need to be B2B based....Use images that compliment the TEXT and speak to a BUSINESS OWNER and NOT A CONSUMER!!
Should not have
• DO NOT CREATE AN AD THAT IS B2C based, this is a B2B ad. please check website www.brightlanepromotionhub.biz

```html
<!DOCTYPE html>
<html lang="en">
<head>
<meta charset="utf-8">
<title>Banner Ad Concepts</title>
<link href="https://fonts.googleapis.com/css2?family=Montserrat:wght@600;700&family=Mulish:ital,wght@0,400;0,500;1,800&family=Poppins:wght@600;700;800&display=swap" rel="stylesheet">
<style>
  :root{
    --page:#f2f2f0;
    --blue:#1478c8;
    --blue-deep:#0b4fa0;
    --blue-bright:#25a6f0;
    --ink:#1d1d1d;
    --black:#151515;
    --white:#ffffff;
    --plate:#e6ecec;
  }
  *{margin:0;padding:0;box-sizing:border-box}
  html,body{width:1200px;height:444px;overflow:hidden;background:var(--page)}
  .board{position:relative;width:1200px;height:444px}
  .ad{position:absolute;top:0;left:0;width:600px;height:600px;overflow:hidden;transform-origin:0 0}
  .ad--gadgets{transform:translate(54px,46px) scale(.5583)}
  .ad--dining{transform:translate(428px,46px) scale(.5583);background:var(--blue)}
  .ad--hotel{transform:translate(810px,46px) scale(.5583)}
  .photo{position:absolute}
  .brand{position:absolute;font-family:'Mulish',sans-serif;font-weight:500;color:var(--white);display:flex;align-items:center;gap:6px;letter-spacing:.5px}
  .brand-dot{display:inline-block;border-radius:50%;background:var(--white)}
  .cta{position:absolute;border-radius:30px;font-family:'Montserrat',sans-serif;font-weight:700;display:flex;align-items:center;justify-content:center;letter-spacing:1px;box-shadow:3px 4px 6px rgba(0,0,0,.35)}

  /* Concept 1 */
  .ad--gadgets .backdrop{position:absolute;inset:0}
  .ad--gadgets .watch{left:20px;top:90px;width:320px;height:395px;border-radius:40px;background:linear-gradient(140deg,#5a5a5a,#1a1a1a 60%,#3a3a3a)}
  .ad--gadgets .buds{left:335px;top:355px;width:235px;height:135px;border-radius:60px;background:radial-gradient(circle at 40% 40%,#5b5b5b,#202020 70%)}
  .headline-1{position:absolute;right:32px;top:42px;text-align:right;font-family:'Mulish',sans-serif;color:var(--white)}
  .headline-1 .lead{font-size:29px;font-weight:500;line-height:34px}
  .headline-1 .body{font-size:19.5px;line-height:22.5px;font-weight:500}
  .headline-1 .prize{font-family:'Poppins',sans-serif;font-weight:800;font-size:38px;line-height:43px;color:var(--blue);-webkit-text-stroke:2px var(--white);paint-order:stroke fill;letter-spacing:-.5px;margin:1px 0}
  .headline-1 .amp{color:var(--white);-webkit-text-stroke:0}
  .ad--gadgets .cta{left:30px;top:508px;width:290px;height:48px;background:var(--white);color:var(--ink);font-size:14.5px}
  .ad--gadgets .brand{right:42px;top:510px;font-size:30px}
  .ad--gadgets .brand-dot{width:12px;height:12px}

  /* Concept 2 */
  .headline-2{position:absolute;left:0;right:0;top:28px;text-align:center;font-family:'Mulish',sans-serif;color:var(--white);font-size:15.5px;line-height:25px}
  .headline-2 em{font-weight:800}
  .plate{position:absolute;left:75px;top:92px;width:456px;height:456px}
  .ad--dining .cta{left:41px;top:522px;width:124px;height:43px;background:var(--black);color:var(--white);font-size:12px}
  .ad--dining .brand{right:46px;top:528px;font-size:19px}
  .ad--dining .brand-dot{width:8px;height:8px}

  /* Concept 3 */
  .ad--hotel .room{inset:0;background:radial-gradient(circle at 30% 60%,#6e4a2c 0%,#9a7a58 35%,#d9c6ad 70%,#efe6d9 100%)}
  .ad--hotel .swoosh{position:absolute;inset:0}
  .headline-3{position:absolute;left:36px;top:156px;font-family:'Poppins',sans-serif;font-weight:700;font-size:24.5px;line-height:32.5px;color:var(--black);text-shadow:-2px 0 var(--white),2px 0 var(--white),0 -2px var(--white),0 2px var(--white),1.5px 1.5px var(--white),-1.5px -1.5px var(--white),1.5px -1.5px var(--white),-1.5px 1.5px var(--white)}
  .headline-3 .hl{color:var(--blue)}
  .ad--hotel .brand{left:50px;top:34px;font-size:20px;color:var(--blue-deep)}
  .ad--hotel .brand-dot{width:8px;height:8px;background:var(--blue-deep)}
  .ad--hotel .cta{left:388px;top:510px;width:165px;height:43px;background:var(--white);color:var(--ink);font-size:13.5px;box-shadow:none}
</style>
</head>
<body>
<main class="board">

  <section class="ad ad--gadgets">
    <svg class="backdrop" viewBox="0 0 600 600" aria-hidden="true">
      <rect width="600" height="600" fill="var(--black)"/>
      <polygon points="0,0 35,0 405,600 0,600" fill="var(--blue)"/>
    </svg>
    <div class="photo watch" role="img" aria-label="Smartwatch with colourful app icons on its screen"></div>
    <div class="photo buds" role="img" aria-label="Pair of dark wireless earbuds"></div>
    <div class="headline-1">
      <div class="lead">Boost Responses</div>
      <div class="body">To Your Ads Without<br>Increasing Ad Spend<br>Giving Away Free</div>
      <div class="prize">Smartwatches</div>
      <div class="prize"><span class="amp">&amp;</span> Norvicks</div>
      <div class="body">You Don't Personally<br>Need To Fulfill!</div>
    </div>
    <div class="cta">GET A FREE SAMPLE PACKAGE</div>
    <div class="brand"><span class="brand-dot"></span>Brightlane</div>
  </section>

  <section class="ad ad--dining">
    <p class="headline-2">More Customers During Tough Times Giving Away Free<br><em>Vacation &amp; Dining</em> Vouchers That You Don't Need To Pay For!</p>
    <svg class="plate" viewBox="0 0 456 456" role="img" aria-label="Dinner plate with napkin, fork and knife tied with a festive ribbon">
      <defs>
        <radialGradient id="napkin" cx="50%" cy="50%" r="50%">
          <stop offset="0%" stop-color="#c98e2a"/>
          <stop offset="55%" stop-color="#dfe7e6"/>
          <stop offset="100%" stop-color="#f3f6f5"/>
        </radialGradient>
      </defs>
      <circle cx="228" cy="228" r="226" fill="var(--plate)"/>
      <circle cx="228" cy="228" r="212" fill="none" stroke="#8a9a9a" stroke-width="1.5" stroke-dasharray="10 8"/>
      <circle cx="228" cy="228" r="150" fill="url(#napkin)"/>
    </svg>
    <div class="cta">SIGN UP</div>
    <div class="brand"><span class="brand-dot"></span>Brightlane</div>
  </section>

  <section class="ad ad--hotel">
    <div class="photo room" role="img" aria-label="Hotel room door held open with key tag numbered 206, warm blurred bedroom behind"></div>
    <svg class="swoosh" viewBox="0 0 600 600" aria-hidden="true">
      <path d="M0,500 C250,520 480,440 600,300 L600,600 L0,600Z" fill="var(--white)"/>
      <path d="M0,510 C260,525 490,450 600,320 L600,600 L0,600Z" fill="var(--blue-bright)"/>
      <path d="M0,540 C260,520 470,470 600,400 L600,600 L0,600Z" fill="var(--blue)"/>
      <path d="M0,560 C250,600 470,520 600,470 L600,600 L0,600Z" fill="var(--blue-deep)"/>
    </svg>
    <div class="brand"><span class="brand-dot"></span>Brightlane</div>
    <p class="headline-3">Increase Conversions<br>On Your Website<br>Offering A Free <span class="hl">Hotel Stay</span><br>Or Even A <span class="hl">Smart Watch</span> In<br>Exchange For Their Form<br>Submission!</p>
    <div class="cta">BOOK A DEMO</div>
  </section>

</main>
</body>
</html>
```